Sunny Fibre Folk - HEMP Products store

Sunny Fibre Folk sell the best hemp products on the market online and at markets and expos Australia wide. Our products are mostly cosmetics, oils, lotions, plus some miscellaneous items such as as bags, clothing, household goods. We would like the website to be lighthearted, fun and portray health and happiness.
We don't want too much information on the main page/home page mostly links and buttons and images.
Things to include: buttons that lead to further info and blog. I would like the buttons for info to have a tiny bit of writing on them to entice people to click for the further info they actually want.
What's on section.
About us
Slideshow of featured products
subscription section
sign up for newsletter link.
Contact us link
Feedback section
Shop & shopping cart etc
short blog section with room to add images
spot for video tutorials
useful links.
connect to social media
And any other cool fun stuff you can think of for us.
We currently have a domain with NetBarrow and they use platform Site Loom 4
www.sunnyfibrefolk.example.au
info@sunnyfibrefolk.example.au
Please see our Logo attached.
I also attached a very badly drawn example of a layout that I like

Target Market(s)

All ages. Parents. Health conscious buyers. natural product consumers. Environmentalist.

Coding

Coded - Design and coding required

Number of Pages Required

5+ page

Font styles to use
Sans Serif
Other font styles liked:
• Spahrty girl font. http://www.glyphbarn.example/spahrty-girl.font

Requirements
Nice to have
• green drop shaped buttons - similar shape to the characters.
Should not have
• Prominent pictures of marijuana leaves.

```html
<!DOCTYPE html>
<html lang="en">
<head>
<meta charset="utf-8">
<title>Sunny Fibre Folk — Hemp Products</title>
<link href="https://fonts.googleapis.com/css2?family=Chewy&family=Open+Sans:wght@400;600;700&display=swap" rel="stylesheet">
<style>
:root{
  --green:#3fa34d;
  --green-dark:#2b8a3e;
  --green-light:#8fd18a;
  --ink:#222;
  --text:#666;
  --muted:#8a8a8a;
  --topbar:#4a4a4a;
  --line:#d6d6d6;
  --band:#efefef;
  --fb:#2d62a8;
  --white:#fff;
}
*{box-sizing:border-box;margin:0;padding:0}
html,body{width:1200px;height:3734px;overflow:hidden;background:var(--white)}
body{font-family:"Open Sans",Arial,sans-serif;color:var(--text);position:relative}
.display{font-family:"Chewy","Comic Sans MS","Chalkboard SE",sans-serif;font-weight:400;letter-spacing:1px;white-space:nowrap}
a{color:inherit;text-decoration:none}

/* top bar */
.topbar{position:absolute;left:0;top:0;width:1200px;height:30px;background:var(--topbar);color:#eee;font-size:12px}
.topbar .contact{position:absolute;left:108px;top:7px;display:flex;gap:22px}
.topbar .account{position:absolute;left:676px;top:7px;display:flex;gap:8px}
.topbar .cart{position:absolute;left:938px;top:0;width:150px;height:30px;background:var(--green);color:#fff;text-align:center;line-height:30px}

/* header */
.header{position:absolute;left:0;top:30px;width:1200px;height:100px;background:#fff;z-index:3}
.logo{position:absolute;left:86px;top:20px;width:165px;height:165px;border-radius:50%;background:#fff;box-shadow:0 2px 6px rgba(0,0,0,.12);display:flex;align-items:center;justify-content:center;text-align:center;font-weight:700;font-size:22px;line-height:1.15;color:var(--ink);z-index:4}
.nav{position:absolute;left:362px;top:45px;display:flex;gap:40px;font-size:15px;font-weight:600;color:#555;letter-spacing:.5px}
.nav .active{color:var(--green)}
.nav svg{margin-left:-10px}

/* hero */
.hero{position:absolute;left:0;top:130px;width:1200px;height:530px;background:linear-gradient(90deg,#f4f4f4 0%,#ececec 45%,#e4e4e4 100%);overflow:hidden}
.hero .photo{position:absolute;left:420px;top:0;width:780px;height:520px;background:linear-gradient(90deg,rgba(255,255,255,0) 0%,#e9d6c8 45%,#dcbda8 70%,#f1f1f1 100%)}
.hero h1{position:absolute;left:100px;top:138px;font-size:50px;line-height:54px;color:var(--green)}
.hero p{position:absolute;left:100px;top:262px;width:320px;font-size:14px;line-height:1.5;color:var(--muted)}
.btn-green{display:inline-block;background:var(--green);color:#fff;border-radius:22px;font-size:14px;font-weight:600;text-align:center}
.hero .shop{position:absolute;left:103px;top:325px;width:168px;height:40px;line-height:40px}
.dots{position:absolute;left:560px;top:434px;display:flex;gap:12px}
.dots span{width:14px;height:14px;border-radius:50%;background:#fff}
.hero .swoosh{position:absolute;left:0;top:380px}

/* section titles */
.title{position:absolute;font-size:42px;line-height:50px;color:var(--green)}
.center{left:0;width:1200px;text-align:center}

/* about */
.about p{position:absolute;left:210px;width:780px;text-align:center;font-size:15px;line-height:1.55;color:var(--muted)}
.btn-outline{position:absolute;left:520px;top:893px;width:166px;height:38px;border:1.5px solid #333;border-radius:20px;text-align:center;line-height:35px;font-size:14px;color:#333}

/* what's on */
.whatson{position:absolute;left:0;top:980px;width:1200px;height:440px;border-top:1px solid var(--line);background:#f0f0f0;overflow:hidden}
.whatson .photo{position:absolute;left:440px;top:0;width:760px;height:440px;background:linear-gradient(90deg,#ededed 0%,#d9d9d9 35%,#f3f3f3 65%,#e2e2e2 100%)}
.whatson h2{position:absolute;left:113px;top:80px;font-size:42px;line-height:50px;color:var(--green)}
.whatson p{position:absolute;left:115px;width:440px;font-size:14px;line-height:1.55;color:var(--text)}
.whatson .more{position:absolute;left:120px;top:320px;width:168px;height:40px;line-height:40px}

/* products */
.products h2{top:1444px;color:var(--ink)}
.card{position:absolute;top:1514px;width:239px;height:334px;border:1px solid #cfcfcf;background:#fff}
.card .img{position:absolute;left:30px;top:30px;width:178px;height:160px;border-radius:6px}
.card .name{position:absolute;left:18px;top:234px;font-size:16px;color:var(--ink)}
.card .desc{position:absolute;left:18px;top:258px;font-size:12px;color:var(--muted)}
.card .price{position:absolute;left:18px;top:290px;font-size:20px;color:var(--ink)}
.card .cart-btn{position:absolute;right:14px;top:278px;width:42px;height:42px;border-radius:50%;background:var(--green)}
.arrow{position:absolute;top:1650px}

/* video */
.videos{position:absolute;left:0;top:1905px;width:1200px;height:411px;background:linear-gradient(90deg,#93d38d 0%,#5fb966 50%,#2f9a47 100%)}
.videos h2{top:48px;color:#fff}
.video{position:absolute;top:122px;width:316px;height:214px;border:3px solid #fff}
.video .play{position:absolute;left:50%;top:50%;transform:translate(-50%,-50%)}

/* blogs */
.blogs h2{left:105px;top:2367px}
.post{position:absolute;top:2435px;width:316px}
.post .img{width:316px;height:212px;position:relative}
.post .date{position:absolute;left:0;bottom:0;width:112px;height:26px;background:var(--green-light);color:#fff;font-size:12px;line-height:26px;text-align:center}
.post h3{margin-top:18px;font-size:20px;font-weight:600;color:var(--ink)}
.post p{margin-top:8px;font-size:13px;line-height:1.45;color:var(--muted)}
.post .read{display:block;margin-top:8px;font-size:12px;color:var(--green)}

/* feeds */
.feed{position:absolute;top:2864px;height:318px;border:1px solid #ccc;background:#fff;overflow:hidden}
.feed .head{height:44px;line-height:44px;padding-left:22px;font-size:18px;position:relative}
.feed.fb .head{background:var(--fb);color:#fff}
.feed.tw .head{color:#5aaee8;border-bottom:1px solid #ddd}
.item{position:absolute;left:24px;width:420px}
.item .av{position:absolute;left:0;top:0;width:38px;height:34px;background:linear-gradient(#b9b1a8,#7d756d)}
.item .who{position:absolute;left:60px;top:0;font-size:13px;color:var(--fb)}
.item .body{position:absolute;left:60px;top:20px;width:360px;font-size:11.5px;line-height:1.45;color:var(--muted)}
.item .ago{font-size:11.5px;color:#4aa8d8}
.follow{position:absolute;right:22px;top:14px;width:52px;height:18px;border-radius:3px;background:#e6eef6;border:1px solid #b5c7da}
.scroll{position:absolute;right:6px;top:56px;width:6px;height:110px;background:#bbb;border-radius:3px}

/* newsletter */
.news{position:absolute;left:0;top:3282px;width:1200px;height:100px;background:var(--band)}
.news h2{position:absolute;left:194px;top:32px;font-size:26px;font-weight:400;color:var(--ink);letter-spacing:.5px}
.news .input{position:absolute;left:510px;top:32px;width:364px;height:38px;background:#fff;border:1px solid #ddd;font-size:12px;color:#aaa;line-height:36px;padding-left:14px}
.news .sub{position:absolute;left:874px;top:32px;width:132px;height:38px;background:#333;color:#fff;font-size:17px;line-height:38px;text-align:center}

/* footer */
.footer{position:absolute;left:0;top:3382px;width:1200px;height:352px;background:var(--green-dark);color:#fff}
.fcol{position:absolute;top:56px}
.fcol h4{font-size:18px;font-weight:400;letter-spacing:.5px;margin-bottom:12px}
.fcol li{list-style:none;font-size:13px;line-height:27px}
.social{display:flex;gap:6px;margin-top:8px}
.social span{width:24px;height:24px;border:1.5px solid #fff;border-radius:50%}
.footer .rule{position:absolute;left:137px;top:298px;width:926px;height:1px;background:rgba(255,255,255,.35)}
.footer .copy{position:absolute;left:0;width:1200px;top:314px;text-align:center;font-size:11px;color:rgba(255,255,255,.8)}
</style>
</head>
<body>

<div class="topbar">
  <div class="contact">
    <span>&#9742; 611 402 7730</span>
    <span>&#9993; info@sunnyfibrefolk.example.au</span>
  </div>
  <div class="account"><span>SIGN UP</span><span>|</span><span>LOGIN</span><span>|</span><span>MY ACCOUNT</span></div>
  <div class="cart">CART 0 items</div>
</div>

<header class="header">
  <nav class="nav">
    <a class="active">HOME</a><a>ABOUT US</a><a>PRODUCT</a><a>WHY US</a><a>BLOGS</a><a>CONTACT</a>
    <svg width="16" height="16" viewBox="0 0 16 16"><circle cx="6.5" cy="6.5" r="5" fill="none" stroke="#888" stroke-width="1.6"/><line x1="10.5" y1="10.5" x2="15" y2="15" stroke="#888" stroke-width="1.6"/></svg>
  </nav>
</header>
<div class="logo">Sunny<br>Fibre<br>Folk</div>

<section class="hero">
  <div class="photo" role="img" aria-label="Woman with clear skin touching her face beside two shampoo bottles"></div>
  <h1 class="display">Cosmetics, Oils<br>and Lotions</h1>
  <p>Gentle hemp care for skin and hair, made with love every day</p>
  <a class="btn-green shop">SHOP NOW</a>
  <div class="dots"><span></span><span></span><span></span></div>
  <svg class="swoosh" width="1200" height="150" viewBox="0 0 1200 150">
    <path d="M0 150 Q300 40 600 95 T1200 90 L1200 150 Z" fill="#fff"/>
    <path d="M0 128 Q300 30 600 78" fill="none" stroke="#9a9a9a" stroke-width="3"/>
  </svg>
</section>

<section class="about">
  <h2 class="title display center" style="top:672px">About Our Company</h2>
  <p style="top:735px">Maecenas aliquet velit vel turpis Mauris neque metus malesuada nec ultricies sit amet porttitor mattis enim In massa libero interdum nec interdum vel blandit sed nulla ullamcorper est eget tempor</p>
  <p style="top:797px">cursus neque mi consectetuer mi a ultricies massa est sed nisl Class aptent taciti sociosqu ad litora torquent per conubia nostra per inceptos hymenaeos Proin nulla arcu nonummy luctus dictum eget fermentum et lorem Nunc porta convallis pede</p>
  <a class="btn-outline">LEARN MORE</a>
</section>

<section class="whatson">
  <div class="photo" role="img" aria-label="White cosmetic jars, a pump bottle and a reed diffuser on a soft grey table"></div>
  <h2 class="display">What's on</h2>
  <p style="top:150px">Maecenas aliquet velit vel turpis Mauris neque metus malesuada nec ultricies sit amet porttitor mattis enim In massa libero interdum nec interdum vel blandit sed</p>
  <p style="top:222px">nulla In ullamcorper est eget tempor cursus neque mi consectetuer mi a ultricies massa est sed nisl Class aptent taciti sociosqu ad litora torquent per conubia nostra per i.</p>
  <a class="btn-green more">LEARN MORE</a>
</section>

<section class="products">
  <h2 class="title display center">Featured Products</h2>
  <svg class="arrow" style="left:56px" width="24" height="56" viewBox="0 0 24 56"><path d="M22 2 L3 28 L22 54" fill="none" stroke="#888" stroke-width="2"/></svg>
  <svg class="arrow" style="left:1100px" width="24" height="56" viewBox="0 0 24 56"><path d="M2 2 L21 28 L2 54" fill="none" stroke="#888" stroke-width="2"/></svg>
  <div class="card" style="left:100px"><div class="img" role="img" aria-label="Pink hemp tote bag" style="background:linear-gradient(#fff,#f5c6d3)"></div><div class="name">Product Name</div><div class="desc">porttitor mattis enim ultricies</div><div class="price">$25.99</div><div class="cart-btn"></div></div>
  <div class="card" style="left:349px"><div class="img" role="img" aria-label="White hemp oil bottle" style="background:linear-gradient(#fff,#e2e2e2)"></div><div class="name">Product Name</div><div class="desc">porttitor mattis enim ultricies</div><div class="price">$25.99</div><div class="cart-btn"></div></div>
  <div class="card" style="left:598px"><div class="img" role="img" aria-label="Jar of hemp face cream" style="background:linear-gradient(#fff,#e9d2b0)"></div><div class="name">Product Name</div><div class="desc">porttitor mattis enim ultricies</div><div class="price">$25.99</div><div class="cart-btn"></div></div>
  <div class="card" style="left:847px"><div class="img" role="img" aria-label="Grey knitted hemp scarf" style="background:linear-gradient(#fff,#bdbdbd)"></div><div class="name">Product Name</div><div class="desc">porttitor mattis enim ultricies</div><div class="price">$25.99</div><div class="cart-btn"></div></div>
</section>

<section class="videos">
  <h2 class="title display center">Video Tutorials</h2>
  <div class="video" style="left:107px;background:linear-gradient(#5d7a52,#2f4a2a)" role="img" aria-label="Video: hemp plants growing in a greenhouse"><svg class="play" width="64" height="64" viewBox="0 0 64 64"><circle cx="32" cy="32" r="29" fill="none" stroke="#fff" stroke-width="2.5"/><path d="M26 20 L44 32 L26 44 Z" fill="#fff"/></svg></div>
  <div class="video" style="left:443px;background:linear-gradient(#f0e6df,#d9c2b4)" role="img" aria-label="Video: applying hemp lotion to legs"><svg class="play" width="64" height="64" viewBox="0 0 64 64"><circle cx="32" cy="32" r="29" fill="none" stroke="#fff" stroke-width="2.5"/><path d="M26 20 L44 32 L26 44 Z" fill="#fff"/></svg></div>
  <div class="video" style="left:777px;background:linear-gradient(#7aa266,#2e5a2f)" role="img" aria-label="Video: rows of young hemp plants in a grow house"><svg class="play" width="64" height="64" viewBox="0 0 64 64"><circle cx="32" cy="32" r="29" fill="none" stroke="#fff" stroke-width="2.5"/><path d="M26 20 L44 32 L26 44 Z" fill="#fff"/></svg></div>
</section>

<section class="blogs">
  <h2 class="title display">Latest Blogs</h2>
  <article class="post" style="left:107px"><div class="img" role="img" aria-label="Woman with long wavy hair" style="background:linear-gradient(90deg,#f3f3f3,#a8795a 50%,#ededed)"><span class="date">25 FEB 2017</span></div><h3>Curabitur vel mi sit amet</h3><p>magna malesuada ultrices Ut nisi erat fermen tum vel congue id euismod in elit Fusce que mi consectetuer mi a ultricies massa</p><a class="read">READ MORE</a></article>
  <article class="post" style="left:443px"><div class="img" role="img" aria-label="White skincare jars and bottles on a pale surface" style="background:linear-gradient(#f6f6f6,#dedede)"><span class="date">25 FEB 2017</span></div><h3>Maecenas aliquet velit</h3><p>magna malesuada ultrices Ut nisi erat fermen tum vel congue id euismod in elit Fusce que mi consectetuer mi a ultricies massa</p><a class="read">READ MORE</a></article>
  <article class="post" style="left:777px"><div class="img" role="img" aria-label="Amber oil bottles with lemon slices and green leaves" style="background:linear-gradient(135deg,#f4f0d8,#c08a3c 55%,#6f9a4f)"><span class="date">25 FEB 2017</span></div><h3>Pellentesque nibh libero</h3><p>magna malesuada ultrices Ut nisi erat fermen tum vel congue id euismod in elit Fusce que mi consectetuer mi a ultricies massa</p><a class="read">READ MORE</a></article>
</section>

<section>
  <div class="feed fb" style="left:107px;width:478px">
    <div class="head">Friendbook Feed</div>
    <div class="item" style="top:72px"><div class="av"></div><div class="who">Vestibulum ligula</div><div class="body">Curabitur metus ipsum luctus eu malesuada ut tincidunt sed diam Donec quis mi sed magna hendrerit accumsan Suspendisse risus<br><span class="ago">2 days ago</span></div></div>
    <div class="item" style="top:180px"><div class="av"></div><div class="who">Maecenas aliquet</div><div class="body">Curabitur metus ipsum luctus eu malesuada ut tincidunt sed diam Donec quis mi sed magna hendrerit accumsan Suspendisse risus<br><span class="ago">2 days ago</span></div></div>
  </div>
  <div class="feed tw" style="left:610px;width:473px">
    <div class="head">Chirper Feed<span class="follow"></span></div>
    <div class="scroll"></div>
    <div class="item" style="top:66px"><div class="av"></div><div class="who">Vestibulum ligula</div><div class="body" style="top:16px">@ inceptos hymenaeos</div><div class="body" style="left:0;top:44px;width:410px">Curabitur metus ipsum luctus eu malesuada ut tincidunt sed diam Donec quis mi sed magna hendrerit accumsan Suspendisse risus<br><span class="ago">2 days ago</span></div></div>
    <div class="item" style="top:186px"><div class="av"></div><div class="who">Maecenas aliquet</div><div class="body" style="top:16px">@ inceptos hymenaeos</div><div class="body" style="left:0;top:44px;width:410px">Curabitur iaculis tempus eros Curabitur vel mi sit amet magna malesuada ultrices Ut nisi erat fermentum vel congue id euismod in elit Fusce ultri<br><span class="ago">2 days ago</span></div></div>
  </div>
</section>

<section class="news">
  <h2>NEWSLETTERS SIGN UP</h2>
  <div class="input">Email address</div>
  <div class="sub">Subscribe</div>
</section>

<footer class="footer">
  <div class="fcol" style="left:137px"><h4>USEFULL LINKS</h4><ul><li>Home</li><li>Why Us</li><li>About Company</li><li>Brands</li><li>Products</li></ul></div>
  <div class="fcol" style="left:344px"><h4>MY ACCOUNT</h4><ul><li>Sign In</li><li>My Cart</li><li>Wishlist</li><li>Create an Account</li><li>Sitemap</li></ul></div>
  <div class="fcol" style="left:580px"><h4>RESOURCES</h4><ul><li>Our Support</li><li>Blogs</li><li>Why Us</li><li>FAQ</li><li>Our Shop</li></ul></div>
  <div class="fcol" style="left:817px"><h4>CONTACT US</h4><ul><li>42 Wattle Grove Lane Suite 7</li><li>Brightwater, QLD 4510</li><li>(07) 5501 2840</li><li>hello@sunnyfibrefolk.example.au</li></ul><div class="social"><span></span><span></span><span></span><span></span></div></div>
  <div class="rule"></div>
  <div class="copy">© 2017 Company Name. All right reserved. Term of Use</div>
</footer>

</body>
</html>
```